依頼詳細
明るくポップなイメージでお願いします。
記載事項については添付データを参考にしてください。
イメージ画像も添付してありますが特にこだわりはありませんので、必要事項が入っていればどのようなデザインでも構いません。
年間通して使用するため季節感のないものでお願いします。
記載項目
添付データ参照
希望イメージ
シンプル 複雑
単色 カラフル
暗い 明るい
日常 高級
遊び心 厳粛
未来的 伝統的
女性的 男性的
希望する色
赤系、黄・オレンジ系、無彩色系
納品ファイル
設定なし
補足説明
プレゼントになる景品の画像をご用意いただきたいです。
データ納品後にこちらで差し替える可能性もございますが、そのまま使用する可能性もあるので使用しても問題ない画像を入れてください。
■ 選んだ理由

弊社の企業HPを調べていただいたのだと思いますが、弊社が取り扱っている製品をイラストアイコン化させて掲載されていたことがとても印象強く、社内でも驚きと感動の声があがりました。しっかりと背景を読み込んだうえでご制作いただいたのではないかと思うとお気遣いがとてもうれしく感じました。また、デザインも希望しているものに沿ったデザインで社内で一番好評でした。

■ 提案者全員のお礼・コメント

たくさんのご応募ありがとうございました。本当に素敵なデザインが多くすべての方を当選にしたくなるほど悩みました。裏面までデザインいただいた方もいらっしゃりとても感激いたしました。皆様たくさんのご応募ありがとうございました。

```html
<!DOCTYPE html>
<html lang="ja">
<head>
<meta charset="utf-8">
<title>プレゼントキャンペーン</title>
<link href="https://fonts.googleapis.com/css2?family=M+PLUS+Rounded+1c:wght@500;700;800;900&display=swap" rel="stylesheet">
<style>
  :root {
    --yellow: #fce45a;
    --red: #e8241f;
    --brown: #4a2a17;
    --orange: #f39a1e;
    --orange-pale: #fde9c8;
    --blue: #1f7ac4;
    --pink: #ec5c8f;
    --white: #ffffff;
    --ink: #3a2a1e;
    --dots: #c9b79c;
  }
  * { box-sizing: border-box; margin: 0; padding: 0; }
  html, body { width: 813px; height: 1200px; overflow: hidden; background: var(--white); }
  body { font-family: "M PLUS Rounded 1c", sans-serif; color: var(--ink); }
  .flyer {
    position: relative; width: 813px; height: 1200px; overflow: hidden;
    background: var(--yellow);
  }
  .bunting {
    position: absolute; left: 0; top: 0; width: 813px; height: 70px;
    background: linear-gradient(90deg, #f28c2b, #5fb8e6, #f4d23b, #e8524a, #77c25e, #f28c2b);
    opacity: .55;
  }
  .title {
    position: absolute; left: 0; top: 48px; width: 100%; text-align: center;
    font-weight: 900; font-size: 132px; letter-spacing: 2px; color: var(--red);
    -webkit-text-stroke: 10px var(--white); paint-order: stroke fill;
    line-height: 1;
  }
  .subtitle {
    position: absolute; left: 0; top: 200px; width: 100%; text-align: center;
    font-weight: 900; font-size: 70px; color: var(--brown);
    -webkit-text-stroke: 8px var(--white); paint-order: stroke fill;
    line-height: 1;
  }
  .intro {
    position: absolute; left: 0; top: 304px; width: 100%; text-align: center;
    font-weight: 700; font-size: 19px; line-height: 1.6; color: var(--ink);
    white-space: nowrap;
  }
  .choice-panel {
    position: absolute; left: 34px; top: 388px; width: 745px; height: 318px;
    border: 3px dashed var(--white); border-radius: 14px;
  }
  .choice-lead {
    position: absolute; left: 60px; top: 404px;
    font-weight: 800; font-size: 19px; line-height: 1.55; color: var(--ink);
    white-space: nowrap;
  }
  .cheer {
    position: absolute; left: 588px; top: 404px; width: 180px;
    color: var(--pink); text-align: center;
    font-weight: 800; font-size: 17px; line-height: 1.5;
  }
  .prizes { position: absolute; left: 52px; top: 472px; width: 710px; display: flex; gap: 13px; }
  .prize { position: relative; width: 228px; height: 222px; }
  .prize-photo { position: absolute; inset: 0; border-radius: 4px; }
  .prize-a .prize-photo { background: radial-gradient(circle at 45% 50%, #b23a3a, #5e1a12 80%); }
  .prize-b .prize-photo { background: radial-gradient(circle at 50% 55%, #d0602e, #3d2417 85%); }
  .prize-c .prize-photo { background: radial-gradient(circle at 50% 50%, #e8445a, #f6e1d6 90%); }
  .prize-tag {
    position: absolute; left: 0; top: 0; width: 66px; height: 66px;
    color: var(--white); text-align: center; font-weight: 900;
    display: flex; flex-direction: column; align-items: center; justify-content: center;
  }
  .prize-tag .letter { font-size: 34px; line-height: 1; }
  .prize-tag .label { font-size: 14px; line-height: 1.1; }
  .prize-a .prize-tag { background: var(--red); }
  .prize-b .prize-tag { background: var(--blue); }
  .prize-c .prize-tag { background: var(--pink); }

  .entry-form {
    position: absolute; left: 34px; top: 716px; width: 745px; height: 400px;
    background: var(--white); border: 3px solid var(--orange); overflow: hidden;
  }
  .row { display: flex; border-bottom: 2px solid var(--orange); }
  .row-head { height: 66px; background: var(--orange-pale); }
  .row-head .ask {
    width: 288px; padding: 8px 20px; font-weight: 800; font-size: 18px; line-height: 1.35;
    border-right: 2px solid var(--orange); display: flex; align-items: center;
  }
  .row-head .opt {
    flex: 1; display: flex; align-items: center; justify-content: center;
    font-weight: 700; font-size: 44px; color: var(--ink);
  }
  .row-head .opt + .opt { border-left: 2px dotted var(--orange); }
  .field-label {
    width: 150px; padding-left: 24px; font-weight: 700; font-size: 18px;
    display: flex; align-items: center; border-right: 2px solid var(--orange);
  }
  .row-name, .row-tel { height: 60px; }
  .row-address { height: 94px; }
  .field-body { flex: 1; position: relative; font-weight: 700; font-size: 18px; }
  .field-body .zip { position: absolute; left: 22px; top: 10px; }
  .field-body .pref { position: absolute; right: 36px; top: 30px; }
  .field-body .city { position: absolute; left: 220px; top: 52px; font-size: 14px; line-height: 1.15; }
  .comment { padding: 10px 24px 0; }
  .comment p { font-weight: 700; font-size: 16px; margin-bottom: 2px; }
  .comment .line { height: 30px; border-bottom: 2px dotted var(--dots); }

  .notes {
    position: absolute; left: 34px; top: 1124px; width: 745px;
    font-size: 11.5px; line-height: 1.5; font-weight: 500; color: var(--ink);
  }
</style>
</head>
<body>
<main class="flyer">
  <div class="bunting" role="img" aria-label="カラフルな三角旗の飾り"></div>
  <h1 class="title">プレゼント</h1>
  <h2 class="subtitle">キャンペーン</h2>
  <p class="intro">いつも弊社ウォーターサーバーをご使用いただき、誠にありがとうございます。<br>感謝の気持ちを込めて、プレゼントキャンペーンを開催いたします！</p>

  <div class="choice-panel"></div>
  <p class="choice-lead">下記３つからお好きなプレゼントをお選びいただき、<br>抽選で１名様ずつプレゼントいたします。</p>
  <p class="cheer">たくさんのご応募を<br>お待ちしております♪</p>

  <div class="prizes">
    <div class="prize prize-a">
      <div class="prize-photo" role="img" aria-label="霜降り牛肉の写真"></div>
      <div class="prize-tag"><span class="letter">A</span><span class="label">お肉</span></div>
    </div>
    <div class="prize prize-b">
      <div class="prize-photo" role="img" aria-label="ゆでたカニの写真"></div>
      <div class="prize-tag"><span class="letter">B</span><span class="label">海鮮</span></div>
    </div>
    <div class="prize prize-c">
      <div class="prize-photo" role="img" aria-label="いちごのスイーツの写真"></div>
      <div class="prize-tag"><span class="letter">C</span><span class="label">スイーツ</span></div>
    </div>
  </div>

  <section class="entry-form">
    <div class="row row-head">
      <div class="ask">ご希望のプレゼントに<br>〇をつけてください</div>
      <div class="opt">A</div><div class="opt">B</div><div class="opt">C</div>
    </div>
    <div class="row row-name"><div class="field-label">お名前</div><div class="field-body"></div></div>
    <div class="row row-tel"><div class="field-label">お電話番号</div><div class="field-body"></div></div>
    <div class="row row-address">
      <div class="field-label">ご住所</div>
      <div class="field-body">
        <span class="zip">〒　　　　−</span>
        <span class="pref">都道府県</span>
        <span class="city">市区<br>郡</span>
      </div>
    </div>
    <div class="comment">
      <p>ご意見やご感想等がございましたらご記入ください</p>
      <div class="line"></div>
      <div class="line"></div>
    </div>
  </section>

  <p class="notes">【注意事項】※必要事項に不備がある場合は無効となります。※ご応募いただいた方の個人情報は、当選者への賞品発送およびご連絡のみに使用いたします。※当選者の発表は賞品の発送をもってかえさせていただきます。※賞品の内容は予告なく変更となる場合がございます。※ご応募はお一人様一回限りとさせていただきます。※賞品の転売・譲渡はご遠慮ください。※応募用紙は弊社配送スタッフにお渡しいただくか、次回のお届け時にご返却ください。※本キャンペーンについてのお問い合わせは弊社窓口までお願いいたします。</p>
</main>
</body>
</html>
```